Letterhead design - Ferrowby Group

We have just had our Logo created and our now wantng a letterhead design to incorporate this. Please use the same colours as in the logo, which is attached.
Please use the company details below
P O Box 86, Kelverton 7315
Ph: 03 491 2753
dale@ferrowbygroup.co.nz
We would like a professional look
We need an overall letterhead design for our varied group of buisinesses which are based in NZ and overseas. We grow and develop buisinesses. Our companies began in NZ but we now have branches overseas as well. People are our greatest asset and we employ some incredible staff. Our buisinesses are scientific, innovative and growing in size and expertise with a financial base.

Target Market(s)

Professionals

Industry/Entity Type

Investment

Requirements
Must have
• Easy to read.
• Please use the same colours as in the logo
• Please use the company details below
• P O Box 86, Kelverton 7315
• Ph: 03 491 2753
• dale@ferrowbygroup.co.nz

```html
<!DOCTYPE html>
<html lang="en">
<head>
<meta charset="utf-8">
<title>Ferrowby Group Letterhead</title>
<link href="https://fonts.googleapis.com/css2?family=Source+Sans+3:wght@400;700&family=Dancing+Script:wght@600&display=swap" rel="stylesheet">
<style>
  :root {
    --brand-green: #27b56e;
    --brand-grey: #6a6a6a;
    --text-dark: #3b3b3b;
    --text-black: #1e1e1e;
    --paper: #ffffff;
  }
  * { margin: 0; padding: 0; box-sizing: border-box; }
  html, body { width: 909px; height: 1200px; overflow: hidden; background: var(--paper); }
  .letterhead {
    position: relative;
    width: 909px;
    height: 1200px;
    background: var(--paper);
    font-family: "Source Sans 3", sans-serif;
    color: var(--text-dark);
  }
  .brand {
    position: absolute;
    top: 46px;
    left: 0;
    width: 100%;
    display: flex;
    justify-content: center;
    align-items: center;
    gap: 12px;
  }
  .brand-mark {
    width: 36px;
    height: 36px;
    background: var(--brand-green);
  }
  .brand-name {
    font-size: 40px;
    font-weight: 700;
    color: var(--brand-green);
    letter-spacing: 0.3px;
  }
  .letter-body {
    position: absolute;
    top: 276px;
    left: 47px;
    width: 831px;
  }
  .salutation {
    font-size: 17.5px;
    font-weight: 700;
    color: var(--brand-green);
    letter-spacing: 0.3px;
    margin-bottom: 16px;
  }
  .letter-body p.paragraph {
    font-size: 16.6px;
    line-height: 29px;
    text-align: justify;
    margin-bottom: 32px;
  }
  .closing {
    margin-top: 42px;
    font-size: 16.5px;
    color: var(--text-black);
  }
  .signature {
    font-family: "Dancing Script", cursive;
    font-size: 31px;
    color: var(--brand-grey);
    margin-top: 0;
    line-height: 1.1;
  }
  .contact-bar {
    position: absolute;
    left: 0;
    bottom: 0;
    width: 909px;
    height: 56px;
    display: flex;
    color: #fff;
    font-size: 20px;
  }
  .contact-item {
    display: flex;
    align-items: center;
    gap: 12px;
    height: 100%;
  }
  .contact-address { width: 374px; background: var(--brand-green); padding-left: 46px; }
  .contact-phone { width: 196px; background: var(--brand-grey); padding-left: 24px; }
  .contact-email { flex: 1; background: var(--brand-green); padding-left: 22px; font-size: 19px; }
  .contact-icon { width: 20px; height: 20px; flex: none; }
</style>
</head>
<body>
<div class="letterhead">
  <header class="brand">
    <span class="brand-mark"></span>
    <span class="brand-name">Ferrowby Group</span>
  </header>

  <main class="letter-body">
    <p class="salutation">Dear Mr. HALE,</p>
    <p class="paragraph">Lorem ipsum dolor sit amet, consectetuer adipiscing elit, sed diam nonummy nibh euismod tincidunt ut laoreet dolore magna aliquam erat volutpat. Ut wisi enim ad minim veniam, quis nostrud exerci tation ullamcorper suscipit lobortis nisl ut aliquip ex ea commodo consequat. Duis autem vel eum iriure dolor in hendrerit in vulputate velit esse molestie consequfeugiat nulla facilisis at vero eros et accumsan et iusto odio dignissim qui blandit praesent luptatum zzril delenit augue duis dolore te feugait nulla facilisi.</p>
    <p class="paragraph">Lorem ipsum dolor sit amet, consectetuer adipiscing elit, sed diam nonummy nibh euismod tincidunt ut laoreet dolore magna aliquam erat volutpat. Ut wisi enim ad minim veniam, quis nostrud exerci tation ullamcorper suscipit lobortis nisl ut aliquip ex ea commodo consequat. Duis autem vel eum iriure dolor in hendrerit in vulputate velit esse molestie consequat, vel illum dolore efacilisis at vero eros et accumsan et iusto odio dignissim qui blandit praesent luptatum zzril delenit augue duis dolore te feugait nulla facilisi.</p>
    <p class="paragraph">Lorem ipsum dolor sit amet, consectetuer adipiscing elit, sed diam nonummy nibh euismod tincidunt ut laoreet dolore magna aliquam erat volutpat. Ut wisi enim ad minim veniam, quis nostrud exerci tation ullamcorper suscipit lobortis nisl ut aliquip ex ea commodo consequat. Duis autem vel eum iriure dolor in hendrerit in vulputate velit esse molestie dolore efacilisis at vero eros et accumsan et iusto odio dignissim qui blandit praesent luptatum zzril delenit augue duis dolore te feugait nulla facilisi.</p>
    <p class="closing">Sincerely Your,</p>
    <p class="signature">Your Name</p>
  </main>

  <footer class="contact-bar">
    <div class="contact-item contact-address">
      <svg class="contact-icon" viewBox="0 0 20 20" aria-hidden="true">
        <path d="M10 1a6.5 6.5 0 0 0-6.5 6.5C3.5 12.5 10 19 10 19s6.5-6.5 6.5-11.5A6.5 6.5 0 0 0 10 1z" fill="#fff"/>
        <circle cx="10" cy="7.5" r="2.4" fill="var(--brand-green)"/>
      </svg>
      <span>P O Box 86, Kelverton 7315</span>
    </div>
    <div class="contact-item contact-phone">
      <svg class="contact-icon" viewBox="0 0 20 20" aria-hidden="true">
        <circle cx="10" cy="10" r="8.5" fill="none" stroke="#fff" stroke-width="1.6"/>
        <path d="M7.2 5.5l1.6 2.2-1 1.2c.7 1.5 1.8 2.6 3.3 3.3l1.2-1 2.2 1.6-.9 1.6c-3.5-.4-6.8-3.7-7.2-7.2z" fill="#fff"/>
      </svg>
      <span>03 491 2753</span>
    </div>
    <div class="contact-item contact-email">
      <svg class="contact-icon" viewBox="0 0 20 20" aria-hidden="true">
        <circle cx="10" cy="10" r="8.5" fill="none" stroke="#fff" stroke-width="1.6"/>
        <rect x="5.5" y="7" width="9" height="6.5" fill="none" stroke="#fff" stroke-width="1.3"/>
        <path d="M5.5 7l4.5 3.5L14.5 7" fill="none" stroke="#fff" stroke-width="1.3"/>
      </svg>
      <span>dale@ferrowbygroup.co.nz</span>
    </div>
  </footer>
</div>
</body>
</html>
```